Sun Jubilee - Concert Poster

We need a poster for a concert involving 3 bands. Marmaduke, Auntie's Gumbo and Velveteen Ray. The event is called the Sun Jubilee. The poster will be a take away. We plan to print some to give out and some for advertising. Should be something people will want to put up on a wall. The poster should have a psychedelic "flavor", colorful.
Info. that needs to be on the poster: Sun Jubilee - Band Names - Pelham Brook's Music Hall - 4182 Route 17, Felton CA - $10 advance Tix - $12 at Door - for tickets www.pelhambrookmusic. - 21 and Over - March 21 2015 - Doors open at 7:00.

Industry/Entity Type

Event

```html
<!DOCTYPE html>
<html lang="en">
<head>
<meta charset="utf-8">
<title>Sun Jubilee – Concert Poster</title>
<link href="https://fonts.googleapis.com/css2?family=Cinzel:wght@400;700;900&family=Cherry+Swash:wght@700&family=Berkshire+Swash&family=Fredoka:wght@600&family=Righteous&family=Anton&display=swap" rel="stylesheet">
<style>
  :root {
    --frame: #000000;
    --field: #1f8a3a;
    --field-deep: #0f6b2a;
    --swirl-yellow: #f4e21c;
    --swirl-cyan: #37c4e6;
    --swirl-violet: #4a2a9a;
    --swirl-lime: #7ccf3a;
    --title-fill: #f26a21;
    --title-edge: #f8d61a;
    --band-fill: #f8d61a;
    --ink: #111111;
    --paper: #ffffff;
    --sign-red: #d5222a;
  }
  html, body {
    margin: 0;
    width: 900px;
    height: 1200px;
    overflow: hidden;
    background: var(--frame);
  }
  .poster { display: block; width: 900px; height: 1200px; }
  .date { font-family: "Cinzel", serif; font-weight: 900; fill: var(--paper); }
  .venue { font-family: "Cherry Swash", cursive; font-weight: 700; fill: var(--paper); stroke: var(--ink); stroke-width: 2; }
  .address { font-family: "Berkshire Swash", cursive; fill: var(--ink); }
  .event-title { font-family: "Fredoka", sans-serif; font-weight: 600; fill: var(--title-fill); stroke: var(--title-edge); stroke-width: 7; paint-order: stroke; }
  .featuring { font-family: "Cinzel", serif; font-weight: 400; fill: none; stroke: var(--ink); stroke-width: 1.6; }
  .rule { stroke: var(--ink); stroke-width: 3; }
  .band { font-family: "Righteous", sans-serif; fill: var(--band-fill); stroke: var(--ink); stroke-width: 5; paint-order: stroke; }
  .doors { font-family: "Anton", sans-serif; fill: var(--paper); }
  .sign-box { fill: var(--band-fill); stroke: var(--sign-red); stroke-width: 5; }
  .sign-text { font-family: "Righteous", sans-serif; fill: var(--ink); }
  .age { font-family: "Cinzel", serif; font-weight: 700; fill: var(--paper); }
  .price { font-family: "Cinzel", serif; font-weight: 700; fill: var(--paper); stroke: var(--ink); stroke-width: 1.5; paint-order: stroke; }
  .tickets { font-family: "Anton", sans-serif; fill: var(--paper); }
</style>
</head>
<body>
<svg class="poster" viewBox="0 0 900 1200" xmlns="http://www.w3.org/2000/svg">
  <defs>
    <radialGradient id="swirl" cx="60" cy="600" r="700" gradientUnits="userSpaceOnUse">
      <stop offset="0" style="stop-color:var(--swirl-violet)"/>
      <stop offset="0.13" style="stop-color:var(--swirl-cyan)"/>
      <stop offset="0.26" style="stop-color:var(--swirl-yellow)"/>
      <stop offset="0.4" style="stop-color:var(--swirl-lime)"/>
      <stop offset="0.7" style="stop-color:var(--field)"/>
      <stop offset="1" style="stop-color:var(--field-deep)"/>
    </radialGradient>
  </defs>

  <rect class="backdrop" x="22" y="30" width="843" height="1128" fill="url(#swirl)" role="img" aria-label="Psychedelic swirling rainbow background with a guitar outline"/>

  <text class="date" x="442" y="80" font-size="52" text-anchor="middle" textLength="505" lengthAdjust="spacingAndGlyphs">March 21, 2015</text>

  <text class="venue" x="432" y="228" font-size="62" text-anchor="middle" textLength="600" lengthAdjust="spacingAndGlyphs">Pelham Brook's</text>
  <text class="address" x="435" y="266" font-size="36" text-anchor="middle" textLength="545" lengthAdjust="spacingAndGlyphs">4182 Route 17,  Felton CA</text>

  <text class="event-title" x="440" y="468" font-size="200" text-anchor="middle" textLength="812" lengthAdjust="spacingAndGlyphs">Sun Jubilee</text>

  <text class="featuring" x="437" y="552" font-size="50" text-anchor="middle" textLength="362" lengthAdjust="spacingAndGlyphs">Featuring</text>
  <line class="rule" x1="256" y1="559" x2="620" y2="559"/>

  <text class="band" x="455" y="640" font-size="78" text-anchor="middle" textLength="360" lengthAdjust="spacingAndGlyphs">Marmaduke</text>
  <text class="band" x="455" y="728" font-size="78" text-anchor="middle" textLength="530" lengthAdjust="spacingAndGlyphs">Auntie's Gumbo</text>
  <text class="band" x="457" y="814" font-size="78" text-anchor="middle" textLength="536" lengthAdjust="spacingAndGlyphs">Velveteen Ray</text>

  <text class="doors" x="170" y="902" font-size="58" textLength="158" lengthAdjust="spacingAndGlyphs">Doors</text>
  <g class="open-sign" transform="rotate(-9 465 895)">
    <rect class="sign-box" x="412" y="874" width="106" height="42"/>
    <text class="sign-text" x="465" y="903" font-size="24" text-anchor="middle">OPEN</text>
  </g>
  <text class="doors" x="580" y="902" font-size="58" textLength="170" lengthAdjust="spacingAndGlyphs">at 7:00</text>

  <text class="age" x="446" y="984" font-size="38" text-anchor="middle" textLength="250" lengthAdjust="spacingAndGlyphs">21 &amp; Over</text>
  <text class="price" x="434" y="1044" font-size="44" text-anchor="middle" textLength="525" lengthAdjust="spacingAndGlyphs">$10 advance Tix</text>
  <text class="price" x="455" y="1094" font-size="44" text-anchor="middle" textLength="380" lengthAdjust="spacingAndGlyphs">$12 at Door</text>

  <text class="tickets" x="445" y="1146" font-size="46" text-anchor="middle" textLength="770" lengthAdjust="spacingAndGlyphs">For tickets visit www.pelhambrookmusic.com</text>
</svg>
</body>
</html>
```